Design for Certificate

Design a certificate for training, providing our company logo such as attachments. Company's name is "BRYNE Fjellvik Advisory Ltd", please refer to our company profile: https://www.bryne-fjellvik.example/company_info

The style of the current certificate is also attached, and another certificate of another company can be referred to. Psd & jpg are required for the final draft (the layers of psd are not merged). Thanks!

```html
<!DOCTYPE html>
<html lang="en">
<head>
<meta charset="utf-8">
<title>Certificate of Completion – BRYNE Fjellvik Advisory Ltd</title>
<link rel="stylesheet" href="https://fonts.googleapis.com/css2?family=Tinos:wght@400;700&display=swap">
<style>
  :root {
    --backdrop: #a8a8a8;
    --paper: #ffffff;
    --ink: #111111;
    --rule: #333333;
    --frame: #555555;
    --brand-dark: #3b3e3f;
    --brand-light: #d9b39a;
    --wave-top: rgba(235, 235, 235, 0);
    --wave-bottom: #ececec;
  }
  * { margin: 0; padding: 0; box-sizing: border-box; }
  html, body {
    width: 1200px; height: 917px; overflow: hidden;
    background: var(--backdrop);
    font-family: "Tinos", "Times New Roman", serif;
    color: var(--ink);
  }
  .certificate {
    position: absolute; left: 283px; top: 53px;
    width: 572px; height: 807px;
    background: var(--paper);
    overflow: hidden;
  }
  .wave-field {
    position: absolute; left: 0; top: 470px; width: 572px; height: 337px;
    background: linear-gradient(172deg, var(--wave-top) 0%, var(--wave-bottom) 55%, #f3f3f3 100%);
  }
  .frame { position: absolute; inset: 0; pointer-events: none; }
  .brand-block {
    position: absolute; left: 230px; top: 40px; width: 111px; height: 111px;
    background: var(--brand-dark);
    display: flex; align-items: center; justify-content: center;
    font-size: 22px; font-weight: 400; color: var(--brand-light);
    letter-spacing: 1px;
  }
  .cert-number {
    position: absolute; left: 363px; top: 39px;
    font-size: 12.5px; display: flex; align-items: flex-end;
  }
  .cert-number .blank {
    display: inline-block; width: 84px; border-bottom: 1px solid var(--rule);
    margin-left: 6px; height: 12px;
  }
  .centered { position: absolute; left: 0; width: 572px; text-align: center; }
  .title { top: 196px; font-size: 26px; font-weight: 700; letter-spacing: 0.3px; }
  .awarded { top: 281px; font-size: 15.5px; }
  .recipient-line {
    position: absolute; left: 99px; top: 360px; width: 373px;
    border-top: 1px solid var(--rule);
  }
  .completed { top: 371px; font-size: 14px; }
  .course { top: 446px; font-size: 21.5px; font-weight: 700; line-height: 34px; }
  .duration {
    position: absolute; left: 139px; top: 574px;
    font-size: 14px; display: flex; align-items: flex-end;
  }
  .duration .blank {
    display: inline-block; width: 141px; border-bottom: 1px solid var(--rule);
    margin-left: 12px; height: 12px;
  }
  .issuer-name {
    position: absolute; left: 36px; top: 701px;
    font-size: 25px; font-weight: 700; white-space: nowrap;
  }
  .issuer-mark {
    position: absolute; left: 244px; top: 647px; width: 84px; height: 124px;
    background: var(--brand-dark);
  }
  .signature {
    position: absolute; left: 353px; top: 721px; width: 175px;
    border-top: 1px solid var(--rule);
    padding-top: 8px;
    font-size: 10.5px; text-align: center; letter-spacing: 0.2px;
  }
</style>
</head>
<body>
  <main class="certificate">
    <div class="wave-field" role="img" aria-label="Soft grey flowing wave-line background pattern"></div>

    <svg class="frame" width="572" height="807" viewBox="0 0 572 807" aria-hidden="true">
      <g stroke="var(--frame)" stroke-width="1" stroke-dasharray="2 2" fill="none">
        <line x1="14" y1="0" x2="14" y2="807"/>
        <line x1="18" y1="0" x2="18" y2="807"/>
        <line x1="554" y1="0" x2="554" y2="807"/>
        <line x1="558" y1="0" x2="558" y2="807"/>
        <line x1="0" y1="16" x2="572" y2="16"/>
        <line x1="0" y1="20" x2="572" y2="20"/>
        <line x1="0" y1="787" x2="572" y2="787"/>
        <line x1="0" y1="791" x2="572" y2="791"/>
      </g>
    </svg>

    <div class="brand-block">BRYNE</div>
    <div class="cert-number">Certificate NO:<span class="blank"></span></div>

    <h1 class="centered title">CERTIFICATE OF COMPLETION</h1>
    <p class="centered awarded">THIS CERTIFICATE IS AWARDED TO</p>
    <div class="recipient-line"></div>
    <p class="centered completed">has successfully completed</p>
    <h2 class="centered course">BRAND REPUTATION MANAGEMENT<br>TRAINING COURSE</h2>
    <p class="duration">Sxteen hours, hold on<span class="blank"></span></p>

    <div class="issuer-name">BRYNE Fjellvik</div>
    <div class="issuer-mark"></div>
    <div class="signature">CHIEF TECHNOLOGY OFFICER</div>
  </main>
</body>
</html>
```